Verin Court Nine Flash website

we need a website to cater to 2 aspect of the business. We have Verin court residence and verin court office. For the office, we will get their inquire and arrange a face to face meetup to show them the office area for rent. For the residence side, it will need to be like lodgly or staymira.com. we want to allow them to book online for the date they need. We have a total of 10 different room configurations starting at $70 per night and up depending on the size of the room. example of the design is https://pelvandale.com/

Target Market(s)

the website should have detail information on the layout, designs, and luxury of the building.

Industry/Entity Type

office and service appartment rental/lease

Coding

Coded - Design and coding required

Number of Pages Required

5+ page

Requirements
Must have
• a luxury perspective
Nice to have
• example https://pelvandale.com/

```html
<!DOCTYPE html>
<html lang="en">
<head>
<meta charset="utf-8">
<title>Verin Court Nine – Luxury Apartments</title>
<link href="https://fonts.googleapis.com/css2?family=Old+Standard+TT:wght@400;700&family=Arimo:wght@400;600;700&display=swap" rel="stylesheet">
<style>
:root{
  --gold:#d49b2a;
  --gold-soft:#e4b75b;
  --cream:#f4e4c4;
  --cream-light:#fbf4e6;
  --ink:#2f2f2f;
  --muted:#6b6b6b;
  --line:#e3d6bd;
  --green:#3d5a2c;
  --dark:#2a1a0c;
  --white:#ffffff;
}
*{box-sizing:border-box;margin:0;padding:0}
html,body{width:1200px;height:4501px;overflow:hidden;background:var(--white)}
body{font-family:"Arimo",Arial,sans-serif;color:var(--ink);font-size:11px;line-height:1.55}
.page{position:relative;width:1200px;height:4501px;overflow:hidden}
.abs{position:absolute}
.serif{font-family:"Old Standard TT",Georgia,serif}
h2.section-title{position:absolute;font-family:"Old Standard TT",Georgia,serif;font-weight:400;font-size:27px;color:var(--ink);letter-spacing:.3px;white-space:nowrap;line-height:1.2}
.btn{position:absolute;display:flex;align-items:center;justify-content:center;gap:7px;height:29px;padding:0 18px;background:var(--gold);color:#fff;font-weight:600;font-size:11px;border-radius:2px;white-space:nowrap}
.btn svg{width:13px;height:8px}
.photo{position:absolute}
p.body{position:absolute;font-size:11px;color:var(--muted);line-height:1.65}
.eyebrow{position:absolute;font-size:10.5px;font-weight:600;color:var(--gold);letter-spacing:.6px;text-transform:uppercase;white-space:nowrap}

/* hero */
.hero{left:70px;top:0;width:1130px;height:594px;background:linear-gradient(160deg,#6fa6d8 0%,#3d78b8 35%,#24507f 60%,#1d3a4f 80%,#3c4d2c 100%)}
.side-social{left:0;top:0;width:70px;height:594px;background:#fff}
.side-social span{position:absolute;left:27px;width:16px;height:16px;border:1.6px solid var(--gold);border-radius:50%}
.brand{left:148px;top:22px;width:160px;text-align:center;color:#fff;font-family:"Old Standard TT",serif;font-size:12px;letter-spacing:.5px;white-space:nowrap}
.brand .mark{display:block;width:22px;height:22px;margin:0 auto 6px;border:1.5px solid #fff;border-radius:50%}
.nav{right:25px;top:44px;display:flex;gap:28px;color:#fff;font-weight:600;font-size:12px}
.hero-eyebrow{left:173px;top:212px;color:#fff;font-size:11.5px}
.hero-title{left:173px;top:222px;color:#fff;font-family:"Old Standard TT",serif;font-size:54px;letter-spacing:1.5px;font-weight:400;white-space:nowrap}
.hero-copy{left:173px;top:300px;width:480px;color:#eef;font-size:10.5px;line-height:1.6}
.btn.green{background:var(--green)}
.btn.outline{background:#fff;color:var(--gold);border:1px solid var(--gold)}
.ring{position:absolute;border:3px solid #fff;border-radius:50%;overflow:hidden}
.ring div{width:100%;height:100%}
.arrow-dot{position:absolute;top:554px;width:22px;height:22px;border-radius:50%;background:#fff;display:flex;align-items:center;justify-content:center}
.stats{left:173px;top:550px;width:730px;height:114px;background:#fff;display:flex;align-items:center}
.stat{flex:1;text-align:center;font-family:"Old Standard TT",serif;font-size:11.5px;position:relative}
.stat+.stat::before{content:"";position:absolute;left:0;top:22px;height:34px;border-left:1px solid var(--line)}
.stat svg{width:30px;height:30px;display:block;margin:0 auto 8px}
.stat b{display:block;font-weight:400;margin-top:2px}

/* features */
.feature{position:absolute;top:1783px;width:201px;height:207px;border:1px solid var(--line);background:#fff;text-align:center}
.feature.alt{background:var(--cream-light)}
.feature svg{width:60px;height:64px;margin-top:30px}
.feature h3{font-family:"Old Standard TT",serif;font-weight:400;font-size:15px;margin-top:12px}
.feature p{font-size:9.5px;color:var(--muted);margin:14px 14px 0;line-height:1.7}

/* plans */
.tabs{left:173px;top:2168px;width:853px;height:40px;border:1px solid var(--gold-soft);font-family:"Old Standard TT",serif;font-size:12px}
.tabs span{position:absolute;top:0;height:38px;line-height:38px;text-align:center}
.tabs .active{border-left:1px solid var(--gold-soft);border-right:1px solid var(--gold-soft);background:#fff}
.specs{left:874px;top:2286px;width:152px}
.specs div{display:flex;justify-content:space-between;height:35px;font-family:"Old Standard TT",serif;font-size:12px}
.specs span:first-child{color:var(--gold)}
.date-field{position:absolute;height:32px;background:var(--cream);border:1px solid #e8d3a8;color:#8a7a60;font-size:10px;padding:0 10px;display:flex;align-items:center;justify-content:space-between}
.date-field svg{width:12px;height:12px}

/* testimonial */
.testi{left:0;top:2554px;width:1200px;height:387px;background:radial-gradient(ellipse at 55% 70%,#5a3a24 0%,#2b2520 45%,#1a1a1c 100%)}
.stars{left:465px;top:2688px;color:var(--gold-soft);font-size:15px;letter-spacing:2px}

/* blogs */
.blog{position:absolute;top:3087px;width:213px;height:254px;color:#fff}
.blog .num{position:absolute;top:-24px;right:14px;font-family:"Old Standard TT",serif;font-size:46px;font-weight:700;color:var(--gold);line-height:1}
.blog .meta{position:absolute;left:14px;right:14px;bottom:14px;display:flex;justify-content:space-between;font-size:9px}

/* contact */
.field{position:absolute;height:44px;background:var(--cream);border:1px solid #e8d3a8;color:#9a8a70;font-size:10px;padding:0 18px;line-height:44px;white-space:nowrap}
.big-num{position:absolute;font-family:"Old Standard TT",serif;font-size:18px;color:var(--gold);font-weight:700}
.num-label{position:absolute;font-family:"Old Standard TT",serif;font-size:11px;white-space:nowrap}

/* location */
.loc-row{position:absolute;display:flex;align-items:center;font-size:10px;width:210px}
.loc-row svg{width:28px;height:28px;margin-right:10px;flex:none}
.loc-row .k{font-family:"Old Standard TT",serif;color:var(--gold);width:80px}
.loc-row .v{color:var(--muted)}

/* footer */
.footer{left:0;top:4171px;width:1200px;height:330px;background:var(--dark);color:#fff}
.footer .wordmark{position:absolute;left:0;width:1200px;top:178px;text-align:center;font-family:"Old Standard TT",serif;font-size:27px;color:var(--gold);letter-spacing:1px}
.footer .contact{position:absolute;top:222px;display:flex;align-items:center;gap:12px;font-family:"Old Standard TT",serif;font-size:12px;line-height:1.4}
.footer .contact svg{width:30px;height:30px;flex:none}
.footer .copy{position:absolute;left:173px;top:295px;font-size:10px}
.footer .socials{position:absolute;right:174px;top:293px;display:flex;gap:18px}
.footer .socials span{width:17px;height:17px;border:1.6px solid #fff;border-radius:3px}
</style>
</head>
<body>
<div class="page">

  <!-- HERO -->
  <div class="abs side-social" aria-label="Social links">
    <span style="top:175px"></span><span style="top:250px"></span><span style="top:324px"></span><span style="top:399px"></span>
  </div>
  <div class="abs hero" role="img" aria-label="Photo of a glass tower against a blue sky with trees below"></div>
  <div class="abs brand"><span class="mark"></span>VERIN COURT NINE</div>
  <nav class="abs nav"><span>Design</span><span>Location</span><span>Experience</span><span>About Us</span><span>Register Now</span></nav>
  <div class="abs hero-eyebrow">The ultimate luxury experience</div>
  <h1 class="abs hero-title">Luxury Apartments</h1>
  <p class="abs hero-copy">It is a long established fact that a reader will be distracted by the readable content of a page when looking at its layout.</p>
  <div class="btn" style="left:173px;top:351px">Take a Tour <svg viewBox="0 0 13 8"><path d="M0 4h11M8 1l3 3-3 3" stroke="#fff" stroke-width="1.4" fill="none"/></svg></div>
  <div class="btn green" style="left:305px;top:351px">Learn More <svg viewBox="0 0 13 8"><path d="M0 4h11M8 1l3 3-3 3" stroke="#fff" stroke-width="1.4" fill="none"/></svg></div>
  <div class="ring" style="left:708px;top:218px;width:160px;height:160px"><div role="img" aria-label="Photo of a tower under a pink sunset sky" style="background:linear-gradient(#d49fb2,#7a6a9a 55%,#2d3e5c)"></div></div>
  <div class="ring" style="left:914px;top:212px;width:168px;height:168px"><div role="img" aria-label="Photo of a red brick tower with balconies" style="background:linear-gradient(#9cc3e6,#b85b3e 55%,#6b2f20)"></div></div>
  <div class="ring" style="left:1118px;top:218px;width:160px;height:160px"><div role="img" aria-label="Photo of a tower at dusk" style="background:linear-gradient(#d9a0b4,#8f7bb0 60%,#3b4a6a)"></div></div>
  <div class="arrow-dot" style="left:968px"><svg width="12" height="8" viewBox="0 0 13 8"><path d="M13 4H2M5 1L2 4l3 3" stroke="#222" stroke-width="1.6" fill="none"/></svg></div>
  <div class="arrow-dot" style="left:999px"><svg width="12" height="8" viewBox="0 0 13 8"><path d="M0 4h11M8 1l3 3-3 3" stroke="#222" stroke-width="1.6" fill="none"/></svg></div>

  <div class="abs stats">
    <div class="stat"><svg viewBox="0 0 30 30" fill="none" stroke="#d49b2a" stroke-width="1.3"><rect x="4" y="13" width="22" height="8"/><rect x="7" y="9" width="7" height="4"/><path d="M4 21v3M26 21v3"/></svg>Bedrooms<b>08</b></div>
    <div class="stat"><svg viewBox="0 0 30 30" fill="none" stroke="#d49b2a" stroke-width="1.3"><rect x="5" y="4" width="20" height="22"/><path d="M5 16h20M9 20h12"/></svg>Studio<b>06</b></div>
    <div class="stat"><svg viewBox="0 0 30 30" fill="none" stroke="#d49b2a" stroke-width="1.3"><path d="M4 26h6v-5h5v-5h5v-5h6V6"/><path d="M4 26h22V6"/></svg>Stairs<b>16</b></div>
    <div class="stat"><svg viewBox="0 0 30 30" fill="none" stroke="#d49b2a" stroke-width="1.3"><rect x="4" y="4" width="22" height="22"/><path d="M4 4l22 22M9 26V14h12"/></svg>Square Feet<b>2300</b></div>
    <div class="stat"><svg viewBox="0 0 30 30" fill="none" stroke="#d49b2a" stroke-width="1.3"><path d="M3 12l12-7 12 7v14H3z"/><rect x="8" y="15" width="14" height="8"/></svg>Garage<b>03</b></div>
  </div>

  <!-- ABOUT -->
  <div class="photo" role="img" aria-label="Photo of a glass office tower" style="left:222px;top:777px;width:108px;height:122px;background:linear-gradient(#8bb4dc,#3e5f86 60%,#27384d)"></div>
  <div class="photo" role="img" aria-label="Photo of a golden stone hotel tower among skyscrapers" style="left:342px;top:732px;width:267px;height:168px;background:linear-gradient(#6fa3d6,#b8925e 50%,#6a5a44)"></div>
  <div class="photo" role="img" aria-label="Photo of a residential tower with trees" style="left:173px;top:913px;width:230px;height:154px;background:linear-gradient(#3d7bc4,#a7b3c4 55%,#2f5a2c)"></div>
  <div class="photo" role="img" aria-label="Photo of a tall brown apartment tower" style="left:416px;top:913px;width:154px;height:224px;background:linear-gradient(#bcd2e6,#8a6a4e 55%,#4a3a2c)"></div>
  <h2 class="section-title" style="left:653px;top:805px">About Our Verin Court Nine</h2>
  <p class="body" style="left:653px;top:855px;width:375px">It is a long established fact that a reader will be distracted by the readable content of a page when looking at its layout. The point of using Lorem Ipsum is that it has a more-or-less normal distribution of letters, as opposed to using 'Content here, content here', making it look like readable English.</p>
  <p class="body" style="left:653px;top:934px;width:375px">It is a long established fact that a reader will be distracted by the readable content of a page when looking at its layout. The point of using Lorem Ipsum is that it has a more-or-less normal distribution of letters, as opposed to using 'Content here, content here', making it look like readable English.</p>
  <div class="btn" style="left:653px;top:1024px">More About Us <svg viewBox="0 0 13 8"><path d="M0 4h11M8 1l3 3-3 3" stroke="#fff" stroke-width="1.4" fill="none"/></svg></div>

  <!-- BUILDING -->
  <h2 class="section-title" style="left:173px;top:1348px">The building you never need to leave</h2>
  <p class="body" style="left:173px;top:1396px;width:400px">Featuring a refined palette of natural materials, the open living spaces provide a warm counterpoint to the soaring ceilings and full-height windows. Custom herringbone floors and hand-selected stone bring a rich tactility to the rooms.</p>
  <p class="body" style="left:173px;top:1462px;width:380px;color:#444;letter-spacing:.3px">The design for Verinhall came from looking at the city's existing buildings and thinking about which ones you might want to live in, not just look at.</p>
  <div class="btn" style="left:173px;top:1534px">See Our Residences <svg viewBox="0 0 13 8"><path d="M0 4h11M8 1l3 3-3 3" stroke="#fff" stroke-width="1.4" fill="none"/></svg></div>
  <div class="photo" role="img" aria-label="Photo of a bright open-plan office floor" style="left:833px;top:1263px;width:192px;height:128px;background:linear-gradient(#e8e2d8,#b9ab96 60%,#7d6c58)"></div>
  <div class="photo" role="img" aria-label="Video still of a warm-lit conference room" style="left:667px;top:1343px;width:332px;height:239px;background:radial-gradient(ellipse at 50% 30%,#f1c07a,#a4682f 50%,#3c2a1e)"></div>
  <svg class="abs" style="left:818px;top:1448px" width="30" height="34" viewBox="0 0 30 34"><path d="M2 2l26 15L2 32z" fill="#fff"/></svg>
  <div class="photo" role="img" aria-label="Photo of a lobby lounge with armchairs" style="left:583px;top:1525px;width:201px;height:133px;background:linear-gradient(#d7a467,#7b5436 60%,#3a2c22)"></div>

  <!-- FEATURES -->
  <div class="feature" style="left:173px"><svg viewBox="0 0 60 64" fill="none" stroke="#d49b2a" stroke-width="1.5"><rect x="8" y="24" width="16" height="38"/><rect x="24" y="6" width="22" height="56"/><rect x="46" y="30" width="10" height="32"/><path d="M29 14h4M37 14h4M29 24h4M37 24h4M29 34h4M37 34h4M12 34h4M12 44h4"/></svg><h3>Duplex Apartment</h3><p>But I must explain to you how all this mistaken idea of denouncing ...</p></div>
  <div class="feature" style="left:390px"><svg viewBox="0 0 60 64" fill="none" stroke="#d49b2a" stroke-width="1.5"><rect x="6" y="6" width="40" height="14" rx="2"/><path d="M46 13h6v14H28v8"/><rect x="24" y="35" width="8" height="24" rx="2"/></svg><h3>Royal Touch Paint</h3><p>But I must explain to you how all this mistaken idea of denouncing ...</p></div>
  <div class="feature" style="left:608px"><svg viewBox="0 0 60 64" fill="none" stroke="#d49b2a" stroke-width="1.5"><path d="M30 8l18 7v14c0 14-8 24-18 28-10-4-18-14-18-28V15z"/><rect x="23" y="30" width="14" height="11"/><path d="M26 30v-4a4 4 0 0 1 8 0v4"/></svg><h3>Spring Secqurity</h3><p>But I must explain to you how all this mistaken idea of denouncing ...</p></div>
  <div class="feature alt" style="left:825px"><svg viewBox="0 0 60 64" fill="none" stroke="#d49b2a" stroke-width="1.5"><path d="M6 6v56M54 6v56M12 18h36M16 14l-4 4 4 4M44 14l4 4-4 4"/></svg><h3>Large Playground</h3><p>But I must explain to you how all this mistaken idea of denouncing ...</p></div>

  <!-- PLANS + ONLINE BOOKING (residence) -->
  <h2 class="section-title" style="left:0;width:1200px;text-align:center;top:2105px">Paticular Plans</h2>
  <div class="abs tabs">
    <span style="left:90px;width:130px">One Bedroom</span>
    <span class="active" style="left:224px;width:130px">Three Bedrooms</span>
    <span style="left:360px;width:130px">Two Bedrooms</span>
    <span style="left:496px;width:130px">Studio</span>
    <span style="left:632px;width:130px">Penhouse</span>
  </div>
  <p class="body" style="left:173px;top:2251px;width:230px">We leverage our breadth of asset classes, vertically integrated services, unique business model, and in-house development and management expertise</p>
  <div class="eyebrow" style="left:173px;top:2330px">Book your stay · from $70 / night</div>
  <div class="date-field" style="left:173px;top:2352px;width:112px">Check-in <svg viewBox="0 0 12 12" fill="none" stroke="#d49b2a" stroke-width="1.1"><rect x="1" y="2" width="10" height="9"/><path d="M1 5h10M4 1v2M8 1v2"/></svg></div>
  <div class="date-field" style="left:293px;top:2352px;width:112px">Check-out <svg viewBox="0 0 12 12" fill="none" stroke="#d49b2a" stroke-width="1.1"><rect x="1" y="2" width="10" height="9"/><path d="M1 5h10M4 1v2M8 1v2"/></svg></div>
  <div class="btn" style="left:173px;top:2400px">Book Now <svg viewBox="0 0 13 8"><path d="M0 4h11M8 1l3 3-3 3" stroke="#fff" stroke-width="1.4" fill="none"/></svg></div>
  <div class="btn outline" style="left:283px;top:2400px">Download PDF <svg viewBox="0 0 13 8"><path d="M0 4h11M8 1l3 3-3 3" stroke="#d49b2a" stroke-width="1.4" fill="none"/></svg></div>
  <div class="photo" role="img" aria-label="Furnished floor plan of a three bedroom apartment" style="left:454px;top:2251px;width:351px;height:224px;background:linear-gradient(135deg,#e7e1d6,#cfc6b6);border:5px solid #4a5364"></div>
  <div class="abs specs">
    <div><span>Room</span><span>3</span></div>
    <div><span>Total Areas</span><span>250</span></div>
    <div><span>Bathrooms</span><span>2</span></div>
    <div><span>Bathrooms</span><span>2</span></div>
    <div><span>Bathrooms</span><span>Yes</span></div>
  </div>

  <!-- TESTIMONIAL -->
  <div class="abs testi" role="img" aria-label="Photo of a dark boardroom with a long table and leather chairs"></div>
  <h2 class="section-title" style="left:0;width:1200px;text-align:center;top:2607px;color:#fff">Our Testimonial</h2>
  <div class="abs" style="left:208px;top:2662px;width:77px;height:168px;background:var(--gold)"></div>
  <div class="abs" role="img" aria-label="Portrait of a smiling client holding a tablet" style="left:223px;top:2656px;width:158px;height:158px;border-radius:50%;background:linear-gradient(#f2f2f2,#c9c9c9 60%,#3a3f4a)"></div>
  <div class="abs stars">★★★★★</div>
  <p class="body" style="left:465px;top:2720px;width:530px;color:#fff;font-size:10.5px">It is a long established fact that a reader will be distracted by the readable content of a page when looking at its layout. The point of using Lorem Ipsum is that it has a more-or-less normal distribution of letters, as opposed to using 'Content here, content here', making it look like readable English.</p>
  <div class="abs serif" style="left:465px;top:2785px;color:#fff;font-size:12px;font-weight:700">Marcus Ellery</div>
  <div class="abs" style="left:465px;top:2803px;color:#ddd;font-size:10px">Halden architecture firm</div>
  <div class="abs" style="left:247px;top:2860px;color:#fff;font-size:18px">01 <span style="font-size:11px;color:#aaa">| &nbsp;02 &nbsp;| &nbsp;03</span></div>
  <div class="abs" style="left:714px;top:2866px;width:11px;height:11px;background:#fff"></div>
  <div class="abs" style="left:732px;top:2866px;width:11px;height:11px;background:#fff"></div>

  <!-- BLOGS -->
  <h2 class="section-title" style="left:173px;top:3000px">Our Latest Blogs</h2>
  <div class="btn" style="left:931px;top:3005px">View All <svg viewBox="0 0 13 8"><path d="M0 4h11M8 1l3 3-3 3" stroke="#fff" stroke-width="1.4" fill="none"/></svg></div>
  <div class="blog" style="left:173px"><div class="abs" role="img" aria-label="Photo of a dim hotel corridor" style="inset:0;background:linear-gradient(90deg,#2a1d14,#7a5432 50%,#2a1d14)"></div><span class="num">01</span><div class="abs serif" style="left:18px;top:112px;font-size:16px;line-height:1.35;width:180px">There are many variations of passages</div><div class="meta"><span>— 31 Jan 2017</span><span>— Latest News</span></div></div>
  <div class="blog" style="left:386px"><div class="abs" role="img" aria-label="Photo of a lit hallway leading to a window" style="inset:0;background:radial-gradient(ellipse at 50% 55%,#d9a36a,#6c4a2e 60%,#2a1d14)"></div><span class="num">02</span><div class="meta"><span>— 31 Jan 2017</span><span>— Latest News</span></div></div>
  <div class="blog" style="left:599px"><div class="abs" role="img" aria-label="Photo of a hallway with garden view" style="inset:0;background:radial-gradient(ellipse at 50% 55%,#b08a52,#5b3f26 60%,#251a12)"></div><span class="num">03</span><div class="meta"><span>— 31 Jan 2017</span><span>— Latest News</span></div></div>
  <div class="blog" style="left:812px"><div class="abs" role="img" aria-label="Photo of a wood-panelled corridor" style="inset:0;background:linear-gradient(90deg,#2a1d14,#8a5e34 50%,#2a1d14)"></div><span class="num">04</span><div class="meta"><span>— 31 Jan 2017</span><span>— Latest News</span></div></div>

  <!-- CONTACT: OFFICE INQUIRY & VIEWING -->
  <div class="eyebrow" style="left:173px;top:3432px">Verin Court Office · inquire &amp; arrange a viewing</div>
  <h2 class="section-title" style="left:173px;top:3458px">Beyond Business as Usual</h2>
  <div class="field" style="left:173px;top:3521px;width:198px">Name</div>
  <div class="field" style="left:387px;top:3521px;width:199px">Phone</div>
  <div class="field" style="left:173px;top:3586px;width:413px">comment · preferred viewing date and office size</div>
  <div class="btn" style="left:173px;top:3649px;height:28px">Submit <svg viewBox="0 0 13 8"><path d="M0 4h11M8 1l3 3-3 3" stroke="#fff" stroke-width="1.4" fill="none"/></svg></div>
  <p class="body" style="left:667px;top:3466px;width:370px;font-size:10.5px">Our thematic, data-driven investment strategy integrates vision, intuition and experience to target opportunities years in advance.</p>
  <div class="big-num" style="left:690px;top:3528px">412</div><div class="num-label" style="left:667px;top:3560px">Square Areas</div>
  <div class="big-num" style="left:790px;top:3528px">412</div><div class="num-label" style="left:773px;top:3560px">Car Parking</div>

  <!-- LOCATION -->
  <div class="abs" role="img" aria-label="Illustrated golden city map with location pins" style="left:0;top:3840px;width:629px;height:240px;background:radial-gradient(ellipse at 30% 55%,#f1d49a 0%,#f8ebd0 45%,#ffffff 75%)"></div>
  <h2 class="section-title" style="left:651px;top:3795px">Potential Location</h2>
  <p class="body" style="left:651px;top:3838px;width:375px;font-size:10px">With our preserved historical significance and prestigious location, Verin Court offers a classic and luxurious Financial District apartment rental experience. Contact us today for more information about making Verin Court your next home.</p>
  <div class="loc-row" style="left:651px;top:3928px"><svg viewBox="0 0 28 28" fill="none" stroke="#777" stroke-width="1.2"><circle cx="20" cy="8" r="3"/><path d="M2 18c4-3 8 3 12 0s8 3 12 0M2 23c4-3 8 3 12 0s8 3 12 0"/></svg><span class="k">Coast:</span><span class="v">300m</span></div>
  <div class="loc-row" style="left:853px;top:3928px"><svg viewBox="0 0 28 28" fill="none" stroke="#777" stroke-width="1.2"><path d="M3 10l11-6 11 6zM5 10v12M10 10v12M18 10v12M23 10v12M3 24h22"/></svg><span class="k">State Bank:</span><span class="v">180m</span></div>
  <div class="loc-row" style="left:651px;top:3979px"><svg viewBox="0 0 28 28" fill="none" stroke="#777" stroke-width="1.2"><path d="M3 11h22v14H3zM3 11l3-6h16l3 6M10 25v-7h8v7"/></svg><span class="k">Supermarket:</span><span class="v">200m</span></div>
  <div class="loc-row" style="left:853px;top:3979px"><svg viewBox="0 0 28 28" fill="none" stroke="#777" stroke-width="1.2"><rect x="6" y="4" width="16" height="16" rx="3"/><path d="M6 13h16M9 24l3-4M19 24l-3-4"/></svg><span class="k">Railway Station:</span><span class="v">1,800m</span></div>
  <div class="loc-row" style="left:651px;top:4028px"><svg viewBox="0 0 28 28" fill="none" stroke="#777" stroke-width="1.2"><path d="M14 3v22M4 12h20M8 22h12M10 7h8"/></svg><span class="k">Airport:</span><span class="v">2,780m</span></div>
  <div class="loc-row" style="left:853px;top:4028px"><svg viewBox="0 0 28 28" fill="none" stroke="#777" stroke-width="1.2"><rect x="4" y="5" width="20" height="16" rx="3"/><path d="M4 14h20"/><circle cx="9" cy="23" r="2"/><circle cx="19" cy="23" r="2"/></svg><span class="k">Bus Station:</span><span class="v">150m</span></div>
  <div class="loc-row" style="left:651px;top:4079px"><svg viewBox="0 0 28 28" fill="none" stroke="#777" stroke-width="1.2"><rect x="5" y="6" width="18" height="19"/><path d="M14 10v6M11 13h6M11 25v-5h6v5"/></svg><span class="k">Hospital:</span><span class="v">500m</span></div>
  <div class="loc-row" style="left:853px;top:4079px"><svg viewBox="0 0 28 28" fill="none" stroke="#777" stroke-width="1.2"><path d="M2 10l12-6 12 6-12 6zM7 13v7c4 3 10 3 14 0v-7"/></svg><span class="k">University:</span><span class="v">250m</span></div>

  <!-- FOOTER -->
  <footer class="abs footer">
    <div class="abs" style="left:578px;top:96px;width:44px;height:44px;border:1.6px solid var(--gold);border-radius:50%"></div>
    <div class="wordmark">VERIN COURT NINE</div>
    <div class="contact" style="left:173px"><svg viewBox="0 0 30 30" fill="none" stroke="#fff" stroke-width="1.3"><rect x="3" y="8" width="24" height="16"/><path d="M3 8l12 9 12-9"/></svg>info@verincourtnine.asia</div>
    <div class="contact" style="left:473px"><svg viewBox="0 0 30 30" fill="none" stroke="#fff" stroke-width="1.3"><path d="M15 27s-8-9-8-15a8 8 0 0 1 16 0c0 6-8 15-8 15z"/><circle cx="15" cy="12" r="3"/></svg><span>Lumen Quay Road, Harbor<br>Island, Eastvale City</span></div>
    <div class="contact" style="left:842px"><svg viewBox="0 0 30 30" fill="none" stroke="#fff" stroke-width="1.3"><path d="M7 4l5 5-3 3c2 4 5 7 9 9l3-3 5 5-3 3C13 26 4 17 4 7z"/></svg><span>+100 55 010 2020/<br>55 010 321 / 55 010 654</span></div>
    <div class="copy">© Copyright by verincourtnine 2024</div>
    <div class="socials"><span></span><span></span><span></span><span></span><span></span></div>
  </footer>
</div>
</body>
</html>
```